label design peanut butter jar to be marketed internationally for a singapore based company

We need design of 2 labels creamy peanut butter and crunch peanut butter
The design is the same only photo of product
And wording change
The logo norvale remains the same and has to be used logo of peanut has to be used
Some idea designs by our in house designer
Enclosed .
Plus a design of a competitor silver orchard

Target Market(s)

international specially emerging markets

Industry/Entity Type

It Company

Requirements
Must have
• norvale logo
• peanut logo

```html
<!DOCTYPE html>
<html lang="en">
<head>
<meta charset="utf-8">
<title>Norvale Creamy Peanut Butter – Jar Label</title>
<link href="https://fonts.googleapis.com/css2?family=Cinzel:wght@700;900&family=Arimo:wght@400;700&display=swap" rel="stylesheet">
<style>
  :root{
    --purple:#4b1c7c;
    --purple-deep:#321055;
    --orange:#f08a16;
    --orange-light:#f7b03c;
    --glow:#ffe48a;
    --gold-text:#7a4510;
    --ink:#1a1a1a;
    --white:#ffffff;
    --muted:#d9cde8;
    --page:#fbf6c8;
  }
  *{margin:0;padding:0;box-sizing:border-box}
  html,body{width:1200px;height:943px;overflow:hidden}
  body{
    background:radial-gradient(ellipse at 50% 60%, #fffbe6 0%, var(--page) 55%, #f4e98a 100%);
    font-family:'Arimo',Arial,sans-serif;
    position:relative;
  }
  .label{
    position:absolute;left:0;top:0;width:1200px;height:386px;overflow:hidden;
    background:linear-gradient(90deg,var(--orange) 0%,var(--orange-light) 35%,var(--orange-light) 65%,var(--orange) 100%);
  }
  .band-top{position:absolute;left:0;top:0;width:100%;height:44px;background:var(--purple)}
  .band-bottom{position:absolute;left:0;bottom:0;width:100%;height:12px;background:var(--purple)}
  .glow{
    position:absolute;left:390px;top:60px;width:420px;height:320px;border-radius:50%;
    background:radial-gradient(circle,var(--glow) 0%,rgba(255,228,138,.6) 45%,rgba(247,176,60,0) 72%);
  }
  .brand{
    position:absolute;display:flex;align-items:center;gap:8px;
    font-family:'Cinzel',serif;font-weight:900;color:var(--purple);letter-spacing:4px;
  }
  .brand .dot{border-radius:50%;background:var(--purple);display:block}
  .brand--side{font-size:26px;top:78px}
  .brand--side .dot{width:14px;height:14px}
  .brand--center{font-size:46px;top:64px;left:456px}
  .brand--center .dot{width:22px;height:22px}
  .net-weight{position:absolute;left:770px;top:12px;font-size:9px;color:var(--muted);text-align:center;line-height:1.15}
  .product-name{position:absolute;text-align:center;font-family:'Cinzel',serif;font-weight:900;color:var(--gold-text);line-height:1}
  .product-name .sub{display:block;font-weight:700;color:var(--purple)}
  .product-name--side{width:220px;top:136px;font-size:28px}
  .product-name--side .sub{font-size:12px;margin-top:2px}
  .product-name--center{left:400px;width:400px;top:302px;font-size:42px}
  .product-name--center .sub{font-size:15px;margin-top:3px}
  .left-panel{left:104px}
  .right-panel{left:906px}
  .product-photo{
    position:absolute;left:454px;top:163px;width:292px;height:140px;border-radius:50% 50% 40% 40%;
    background:radial-gradient(ellipse at 50% 40%,#d9a35a 0%,#b9772e 55%,#8a5a24 100%);
  }
  .info{position:absolute;left:64px;width:280px;text-align:center}
  .info-head{
    display:inline-block;background:var(--purple);color:var(--white);font-weight:700;font-size:12px;
    padding:2px 16px;border-radius:3px;
  }
  .info-text{color:var(--purple-deep);font-size:11px;line-height:1.45;margin-top:4px}
  .ingredients{top:182px}
  .batch{top:238px}
  .manufacturer{top:293px}
  .maker-box{
    position:absolute;left:69px;top:317px;width:265px;height:48px;background:var(--white);
    padding:6px 8px;font-size:7.5px;color:var(--ink);line-height:1.35;display:flex;gap:8px;
  }
  .maker-box .mark{width:12px;height:12px;border-radius:50%;background:var(--purple);flex:none;margin-top:2px}
  .maker-box strong{font-size:8px}
  .nutrition{
    position:absolute;left:926px;top:182px;width:197px;background:var(--white);
    border:1px solid var(--ink);padding:3px 6px 4px;color:var(--ink);font-size:7px;line-height:1.15;
  }
  .nutrition h3{font-size:16px;font-weight:700;line-height:1.1;border-bottom:1px solid var(--ink);padding-bottom:1px}
  .nutrition .serving{border-bottom:3px solid var(--ink);padding:1px 0 2px}
  .nutrition table{width:100%;border-collapse:collapse}
  .nutrition td{border-bottom:1px solid #999;padding:0;height:9px;line-height:8px}
  .nutrition td.v{text-align:right;width:34px}
  .nutrition .b{font-weight:700}
  .nutrition .hdr td{font-weight:700;border-bottom:2px solid var(--ink)}
  .nutrition tr:last-child td{border-bottom:none}
</style>
</head>
<body>
<section class="label" aria-label="Norvale creamy peanut butter jar label">
  <div class="band-top"></div>
  <div class="glow"></div>

  <div class="brand brand--side left-panel"><span>NORVALE</span><span class="dot"></span></div>
  <div class="product-name product-name--side" style="left:100px">CREAMY<span class="sub">PEANUT BUTTER</span></div>
  <div class="info ingredients">
    <span class="info-head">Ingredients:</span>
    <p class="info-text">Your Text here, your text here, your text here, your text<br>here, your text here, your text here, your text here.</p>
  </div>
  <div class="info batch">
    <span class="info-head">Prod / Exp / Batch</span>
    <p class="info-text">Your Text here, your text here, your text here, your text<br>here, your text here, your text here, your text here.</p>
  </div>
  <div class="info manufacturer"><span class="info-head">Manufactured For</span></div>
  <div class="maker-box">
    <span class="mark"></span>
    <div><strong>Northvale Trading Pte Ltd</strong><br>Singapore 100000<br>E: sales@northvaletrading.com<br>W: www.northvaletrading.com</div>
  </div>

  <div class="brand brand--center"><span>NORVALE</span><span class="dot"></span></div>
  <div class="net-weight">200<br>GRAMS</div>
  <div class="product-photo" role="img" aria-label="Bowl of creamy peanut butter surrounded by peanuts"></div>
  <div class="product-name product-name--center">CREAMY<span class="sub">PEANUT BUTTER</span></div>

  <div class="brand brand--side right-panel"><span>NORVALE</span><span class="dot"></span></div>
  <div class="product-name product-name--side" style="left:900px">CREAMY<span class="sub">PEANUT BUTTER</span></div>
  <div class="nutrition">
    <h3>Nutrition Facts</h3>
    <div class="serving">Serving Size 1-8 oz cup<br>Servings Per Container</div>
    <table>
      <tr><td class="b" style="height:17px">Amount per Serving<br>Calories 0</td><td class="v"></td><td class="v"></td></tr>
      <tr class="hdr"><td></td><td class="v" colspan="2">% Daily Value</td></tr>
      <tr><td class="b">Total Fat</td><td class="v">0.00g</td><td class="v">0.00g</td></tr>
      <tr><td>Saturated Fat</td><td class="v">0.00g</td><td class="v">0.00g</td></tr>
      <tr><td>Trans Fat</td><td class="v">0.00g</td><td class="v">0.00g</td></tr>
      <tr><td>Cholesterol</td><td class="v">0.00g</td><td class="v">0.00g</td></tr>
      <tr><td>Sodium</td><td class="v">0.00g</td><td class="v">0.00g</td></tr>
      <tr><td class="b">Total Carbohydrate</td><td class="v">0.00g</td><td class="v">0.00g</td></tr>
      <tr><td>Dietary Fiber</td><td class="v">0.00g</td><td class="v">0.00g</td></tr>
      <tr><td>Sugars</td><td class="v">0.00g</td><td class="v">0.00g</td></tr>
      <tr><td class="b">Protein</td><td class="v">0.00g</td><td class="v">0.00g</td></tr>
    </table>
  </div>

  <div class="band-bottom"></div>
</section>
</body>
</html>
```